ALL TYPES OF COMMERCIAL PLASTERING

TYPE OF BLOCK LETTERING WITH STAND OUT QUALITIES
WITH SOME TYPE OF LOGO
SOMETHING UNIQUE FOR THE BUILDING INDUSTRY.
QUALITY WORKMANSHIP
Updates

forgot to include my mobile phone number on my brief. could you add it to your design please MOBILE PH 0412 858 196

please let me make this quite clear ,the company name is harbourline linings and Fitouts PTY LTD. THE TYPE OF WORK WE WILL BE DOING IS COMMERCIAL PLASTERING.

Industry/Entity Type

Industry

Contact Information for Business Card

harbourline linings and fitouts P/L
marcus devlin p.o.box 42 wendouree 3355 email address harbourlinelinings@examplemail.com
ABN 51 718 294 605 COMMERCIAL PLASTERING

```html
<!DOCTYPE html>
<html lang="en">
<head>
<meta charset="utf-8">
<title>Harbourline Linings and Fitouts – Business Card</title>
<link rel="stylesheet" href="https://fonts.googleapis.com/css2?family=Saira+Condensed:wght@800&family=Saira:wght@500;600;700&display=swap">
<style>
  :root {
    --stage: #e6e4e1;
    --card-white: #f7f7f7;
    --steel-light: #dcdcdc;
    --steel-mid: #c4c4c4;
    --steel-dark: #8c8c8c;
    --heading-steel: #a9a9ab;
    --ink: #1c1c1c;
    --accent-red: #e4262a;
    --tagline: #9a9a9a;
  }
  * { margin: 0; padding: 0; box-sizing: border-box; }
  html, body {
    width: 1200px; height: 1200px; overflow: hidden;
    background: var(--stage);
  }
  .business-card {
    position: absolute; left: 50px; top: 261px;
    width: 1100px; height: 678px;
    background: var(--card-white);
    overflow: hidden;
    box-shadow: 0 6px 18px rgba(0,0,0,0.18);
  }
  .card-backdrop { position: absolute; inset: 0; width: 100%; height: 100%; }
  .mark-circle {
    position: absolute; left: 114px; top: 94px;
    width: 240px; height: 240px; border-radius: 50%;
    background: radial-gradient(circle at 40% 35%, #f2f2f2, #bdbdbd 75%, #9e9e9e);
  }
  .trade-heading {
    position: absolute; left: 410px; top: 40px;
    font-family: "Saira Condensed", sans-serif; font-weight: 800;
    font-size: 118px; line-height: 108px; letter-spacing: 3px;
    color: var(--heading-steel); text-transform: uppercase;
  }
  .company-name {
    position: absolute; left: 414px; top: 274px;
    font-family: "Saira", sans-serif; font-weight: 700;
    font-size: 22px; letter-spacing: 1px;
    color: var(--tagline); text-transform: uppercase;
  }
  .contact-block {
    position: absolute; left: 46px; top: 418px;
    font-family: "Saira", sans-serif; text-transform: uppercase;
  }
  .person-name {
    font-weight: 600; font-size: 50px; line-height: 60px;
    color: var(--accent-red); letter-spacing: 2px; margin-bottom: 10px;
  }
  .contact-line {
    font-weight: 500; font-size: 28px; line-height: 45px; color: var(--ink);
  }
  .contact-label { color: var(--accent-red); }
</style>
</head>
<body>
  <div class="business-card">
    <svg class="card-backdrop" viewBox="0 0 1100 678" preserveAspectRatio="none" aria-hidden="true">
      <defs>
        <linearGradient id="steel-panel" x1="0" y1="0" x2="1" y2="1">
          <stop offset="0" stop-color="#cfcfcf"/>
          <stop offset="0.5" stop-color="#dedede"/>
          <stop offset="1" stop-color="#d2d2d2"/>
        </linearGradient>
        <linearGradient id="steel-rule" x1="0" y1="0" x2="1" y2="0">
          <stop offset="0" stop-color="#b5b5b5"/>
          <stop offset="0.5" stop-color="#8a8a8a"/>
          <stop offset="1" stop-color="#6f6f6f"/>
        </linearGradient>
      </defs>
      <path d="M0 0 H1100 V678 H1098 C912 396 420 300 0 322 Z" fill="url(#steel-panel)"/>
      <path d="M0 322 C420 300 912 396 1098 678" fill="none" stroke="url(#steel-rule)" stroke-width="7"/>
    </svg>

    <div class="mark-circle" role="img" aria-label="Company emblem"></div>

    <h1 class="trade-heading">Commercial<br>Plastering</h1>
    <p class="company-name">Harbourline linings and fitouts P/L</p>

    <div class="contact-block">
      <p class="person-name">Marcus Devlin</p>
      <p class="contact-line">P.O.Box 42 Wendouree 3355</p>
      <p class="contact-line"><span class="contact-label">ABN</span> : 51 718 294 605</p>
      <p class="contact-line"><span class="contact-label">Phone</span> : 0355 501 724</p>
      <p class="contact-line"><span class="contact-label">Email</span> : harbourlinelinings@examplemail.com</p>
    </div>
  </div>
</body>
</html>
```